Letterhead

Can you please design me a letterhead that I can use electronically in word as a template. I have attached my business card as I would like the design to reflect this logo.

```html
<!DOCTYPE html>
<html lang="en">
<head>
<meta charset="utf-8">
<title>Letterhead</title>
<link rel="stylesheet" href="https://fonts.googleapis.com/css2?family=Arimo:wght@400;700&family=Open+Sans:wght@400;600&family=Pinyon+Script&display=swap">
<style>
  :root {
    --backdrop: #e9e9e9;
    --paper: #ffffff;
    --ink: #3a3a3a;
    --ink-soft: #555555;
    --brand-red: #e0261c;
  }
  * { margin: 0; padding: 0; box-sizing: border-box; }
  html, body {
    width: 1200px;
    height: 795px;
    overflow: hidden;
    background: var(--backdrop);
  }
  .letterhead {
    position: absolute;
    left: 338px;
    top: 27px;
    width: 524px;
    height: 741px;
    background: var(--paper);
    box-shadow: 0 2px 10px rgba(0,0,0,0.08);
    font-family: "Arimo", Arial, sans-serif;
    color: var(--ink);
  }
  .brand {
    position: absolute;
    right: 24px;
    top: 14px;
    text-align: right;
  }
  .brand-name {
    font-family: "Arimo", Arial, sans-serif;
    font-weight: 400;
    font-size: 38px;
    line-height: 1;
    letter-spacing: -0.5px;
    color: var(--brand-red);
  }
  .brand-tagline {
    font-size: 7.5px;
    color: var(--ink);
    margin-top: 1px;
  }
  .letter-body {
    position: absolute;
    left: 76px;
    top: 148px;
    width: 395px;
    font-size: 9px;
    line-height: 1.3;
    color: var(--ink-soft);
  }
  .letter-body h2 {
    font-size: 9px;
    font-weight: 700;
    color: var(--ink);
    margin-bottom: 9px;
  }
  .letter-body p { margin-bottom: 12px; }
  .signature {
    position: absolute;
    left: 92px;
    top: 438px;
    font-family: "Pinyon Script", cursive;
    font-size: 32px;
    color: var(--ink);
  }
  .sender {
    position: absolute;
    left: 88px;
    top: 620px;
    font-family: "Open Sans", Arial, sans-serif;
    font-size: 9.5px;
    color: var(--ink);
  }
  .sender-name { font-weight: 600; margin-bottom: 6px; }
  .sender-role { color: var(--brand-red); font-weight: 400; }
  .contact-line span { margin-right: 8px; }
  .contact-line .contact-label { color: var(--brand-red); margin-right: 1px; }
  .accent-block {
    position: absolute;
    left: 32px;
    top: 596px;
    width: 32px;
    height: 58px;
    background: var(--brand-red);
  }
</style>
</head>
<body>
  <main class="letterhead">
    <header class="brand">
      <div class="brand-name">meridale</div>
      <div class="brand-tagline">Business Consulting Pty Ltd</div>
    </header>

    <section class="letter-body">
      <h2>Lorem Ipsum</h2>
      <p>Lorem Ipsum is simply dummy text of the printing and typesetting industry. Lorem Ipsum has been the industry's standard dummy text ever since the 1500s, when an unknown printer took a galley of type and scrambled it to make a type specimen book. It has survived not only five centuries, but also the leap into electronic typesetting, remaining essentially unchanged. It was popularised in the 1960s with the release of Lettrafix sheets containing Lorem Ipsum passages, and more recently with desktop publishing software like Pagecraft Studio including versions of Lorem Ipsum.</p>
      <p>passages, and more recently with desktop publishing software like Pagecraft Studio including versions of Lorem Ipsum.</p>
      <p>Lorem Ipsum is simply dummy text of the printing and typesetting industry. Lorem Ipsum has been the industry's standard dummy text ever since the 1500s, when an unknown printer took a galley of type and scrambled it to make a type specimen book.</p>
      <p>Lorem Ipsum is simply dummy text of the printing and typesetting industry. Lorem Ipsum has been the industry's standard dummy text ever since the 1500s, when an unknown printer took a galley of type and scrambled it to make a type specimen book. It has survived not only five centuries, but also the leap into electronic typesetting, remaining essentially unchanged.</p>
    </section>

    <div class="signature">Lorem Ipsum</div>

    <div class="accent-block"></div>

    <footer class="sender">
      <div class="sender-name">Clara Whitfield <span class="sender-role">Principal</span></div>
      <div class="contact-line">
        <span class="contact-label">Phone:</span><span>0400 123 456</span>
        <span class="contact-label">Email:</span><span>clara@meridale.net.au</span>
        <span class="contact-label">ACN:</span><span>000 000 000</span>
      </div>
    </footer>
  </main>
</body>
</html>
```